Business Card Design

We are a home improvement and landscaping company based in South Eastern Connecticut hence the name BRIMWAL. Landscaping & Home Renovation are our focus. Im looking for a very professional looking design. Something that will intergrade the two perfectly with bright but comfortable colors. The final design should communicate professionalism and trust worthiness in a place people feel most comfortable with their largest investment, that being their home.
Updates

Project Deadline Extended
Reason: I haven't come across a design that satisfies me.

Project Deadline Extended
Reason: Looking for more designs

Industry/Entity Type

Home Improvement

Contact Information for Business Card

Side one will contain my contact information
BRIMWAL
Landscaping & Home Renovation
Gregory Hallet
5034418952
HIC.0583927
Side two will have a list of services:
Spring/Fall Clean-Ups
Property Management/Mowing
Lawn Care
Brush Clearing
Design Consultation
Interior Home Improvement
Kitchen, Bath & Office
Basement Finishing/Remodel
Flooring
Drywall
Paint
Doors & Windows
Trim & Base

```html
<!DOCTYPE html>
<html lang="en">
<head>
<meta charset="utf-8">
<title>BRIMWAL – Services Card</title>
<link rel="stylesheet" href="https://fonts.googleapis.com/css2?family=Aladin&display=swap">
<style>
  :root {
    --paper: #ffffff;
    --frame-red: #d8141b;
    --frame-cyan: #3fe0ee;
    --foliage-dark: #1f4a14;
    --foliage-mid: #3f7d22;
    --lawn: #5fcf1c;
    --lawn-light: #8ee83a;
    --leaf-dark: #0f3a0a;
    --leaf-mid: #1f7a12;
    --banner: #2f5a1e;
    --banner-edge: #0f2a08;
    --name-fill: #9cf03e;
    --accent-yellow: #fbff5c;
    --ink-shadow: #0b2205;
  }
  * { margin: 0; padding: 0; box-sizing: border-box; }
  html, body { width: 1200px; height: 702px; overflow: hidden; background: var(--paper); }
  .card { position: relative; width: 1200px; height: 702px; background: var(--paper); }
  .frame-outer {
    position: absolute; left: 22px; top: 22px; width: 1158px; height: 658px;
    border: 4px solid var(--frame-red);
  }
  .frame-inner {
    position: absolute; left: 42px; top: 42px; width: 1120px; height: 622px;
    border: 4px solid var(--frame-cyan);
  }
  .scene {
    position: absolute; left: 61px; top: 56px; width: 1086px; height: 592px; overflow: hidden;
  }
  .garden-photo {
    position: absolute; inset: 0;
    background: linear-gradient(180deg, var(--foliage-dark) 0%, var(--foliage-mid) 28%, #4e9a24 42%, var(--lawn) 52%, var(--lawn-light) 62%, var(--lawn) 75%);
  }
  .leaf-pattern { position: absolute; left: 0; top: 0; width: 1086px; height: 592px; }
  .banner {
    position: absolute; left: 0; top: 7px; width: 1086px; height: 59px;
    background: var(--banner); border: 2px solid var(--banner-edge);
    display: flex; align-items: center; justify-content: center;
  }
  .banner-text {
    font-family: "Aladin", cursive; font-size: 50px; color: var(--accent-yellow);
    letter-spacing: 1px;
    text-shadow: -2px 0 var(--ink-shadow), 2px 0 var(--ink-shadow), 0 -2px var(--ink-shadow), 0 2px var(--ink-shadow), 3px 3px 2px var(--ink-shadow);
  }
  .brand-name {
    position: absolute; left: 0; width: 1086px; top: 102px; text-align: center;
    font-family: "Aladin", cursive; font-weight: 400; font-size: 150px; line-height: 1;
    color: var(--name-fill); letter-spacing: 4px;
  }
  .services-heading {
    position: absolute; left: 250px; width: 528px; top: 340px; text-align: center;
    font-family: "Aladin", cursive; font-size: 44px; line-height: 1.1; color: var(--accent-yellow);
    border-bottom: 3px solid var(--accent-yellow); padding-bottom: 2px;
    text-shadow: 2px 2px 2px var(--ink-shadow);
  }
  .service-list {
    position: absolute; left: 0; width: 1086px; top: 400px; text-align: center;
    font-family: "Aladin", cursive; font-size: 35px; color: var(--accent-yellow);
    text-shadow: 2px 2px 2px var(--ink-shadow), -1px -1px 1px var(--ink-shadow);
  }
  .service-line { height: 47px; line-height: 47px; white-space: pre; }
</style>
</head>
<body>
<div class="card">
  <div class="frame-outer"></div>
  <div class="frame-inner"></div>
  <div class="scene">
    <div class="garden-photo" role="img" aria-label="Photo of a landscaped garden with flowering shrubs and a green lawn"></div>
    <svg class="leaf-pattern" viewBox="0 0 1086 592" role="img" aria-label="Decorative sweep of green leaves across the lower part">
      <defs>
        <linearGradient id="leafGrad" x1="0" y1="0" x2="0" y2="1">
          <stop offset="0" stop-color="var(--leaf-mid)"/>
          <stop offset="1" stop-color="var(--leaf-dark)"/>
        </linearGradient>
      </defs>
      <path d="M0 300 C 180 230, 320 250, 430 300 C 560 250, 760 230, 1086 200 L1086 592 L0 592 Z" fill="url(#leafGrad)"/>
    </svg>
    <div class="banner"><span class="banner-text">CALL US TODAY FOR YOUR FREE CONSULTATION</span></div>
    <div class="brand-name">BRIMWAL</div>
    <div class="services-heading">What Services Do We Offer?</div>
    <div class="service-list">
      <div class="service-line">Spring/Fall Clean-Up      Property Management      Mowing &amp; Lawn Care</div>
      <div class="service-line">Brush Clearing,   Design Consultation,   Interior Home Improvement</div>
      <div class="service-line">Kitchen, Bath, &amp; Office   Basement Finishing Remodel,   Flooring,   Drywall,</div>
      <div class="service-line">Paint,   Doors  &amp; Windows,   Trim &amp; Base</div>
    </div>
  </div>
</div>
</body>
</html>
```